HomeBridle business card and stationary design

We are looking for a simple yet elegant design for our mortgage company business card and stationary.

The card should include:
Name (Derek Walsh)
Title (CEO)
Phone Number (614-208-3917)
Address (48 Birchfield Court, Suite 314, Marlow, OH 43952)
Email (email@homebridle-example.com)
"NMLS" i.e. (NMLS 61947)
"Company NMLS" (Company NMLS 472815)

See above

```html
<!DOCTYPE html>
<html lang="en">
<head>
<meta charset="UTF-8">
<title>HomeBridle Business Card</title>
<link href="https://fonts.googleapis.com/css2?family=Montserrat:wght@500&family=Source+Sans+3:wght@400;700&display=swap" rel="stylesheet">
<style>
  :root {
    --page-bg: #e6e6e6;
    --navy: #1a2430;
    --sky: #1ea3dc;
    --paper: #f4f4f4;
    --ink: #2a2f36;
    --white: #ffffff;
  }
  * { margin: 0; padding: 0; box-sizing: border-box; }
  html, body {
    width: 1200px; height: 960px; overflow: hidden;
    background: var(--page-bg);
  }
  .canvas { position: relative; width: 1200px; height: 960px; }

  .card {
    position: absolute; left: 303px; width: 593px; height: 339px;
    overflow: hidden;
  }
  .card-front { top: 119px; background: var(--navy); }
  .card-back { top: 510px; background: var(--paper); }

  .wordmark {
    position: absolute;
    font-family: "Montserrat", sans-serif;
    font-weight: 500;
    letter-spacing: -0.5px;
    white-space: nowrap;
  }
  .card-front .wordmark {
    left: 0; right: 0; top: 138px; text-align: center;
    font-size: 64px; line-height: 1; color: var(--white);
  }
  .card-back .wordmark {
    left: 54px; top: 152px;
    font-size: 36px; line-height: 1; color: var(--navy);
  }

  .divider {
    position: absolute; left: 295px; top: 67px;
    width: 1.5px; height: 204px; background: var(--navy);
  }

  .details {
    position: absolute; left: 322px; top: 64px;
    font-family: "Source Sans 3", sans-serif;
    font-size: 15px; line-height: 20px; color: var(--ink);
  }
  .details .name {
    font-weight: 700; font-size: 20px; line-height: 24px;
    color: var(--sky); letter-spacing: 0.2px;
  }
  .details .label { color: var(--sky); }
  .details .address { margin-top: 17px; }
  .details .contact { margin-top: 5px; }
  .contact-row { display: flex; align-items: center; gap: 6px; }
  .contact-row svg { width: 13px; height: 13px; flex: none; }

  .foot-band { position: absolute; left: 0; bottom: 0; width: 593px; height: 16px; }
</style>
</head>
<body>
<main class="canvas">
  <section class="card card-front">
    <div class="wordmark">HomeBridle</div>
  </section>

  <section class="card card-back">
    <div class="wordmark">HomeBridle</div>
    <div class="divider"></div>
    <div class="details">
      <p class="name">DEREK WALSH</p>
      <p>CEO</p>
      <p><span class="label">NMLS</span> 61947</p>
      <div class="address">
        <p>48 Birchfield Court, Suite 314</p>
        <p>Marlow, OH 43952</p>
        <p><span class="label">Company NMLS</span> 472815</p>
      </div>
      <div class="contact">
        <p class="contact-row">
          <svg viewBox="0 0 16 16" aria-hidden="true"><path fill="#1ea3dc" d="M3.6 1.2l2.3 2.6-1.3 1.8c.9 1.9 2.3 3.3 4.2 4.2l1.8-1.3 2.6 2.3-1.4 2.4C6.8 13 2.9 9.1 1.2 4z"/><path fill="none" stroke="#1ea3dc" stroke-width="1.2" d="M9.5 2.5a4 4 0 0 1 4 4M9.5 .8a5.7 5.7 0 0 1 5.7 5.7"/></svg>
          614-208-3917
        </p>
        <p class="contact-row">
          <svg viewBox="0 0 16 16" aria-hidden="true"><rect x="1" y="3" width="14" height="10" fill="none" stroke="#1ea3dc" stroke-width="1.5"/><path d="M1 3.5l7 5.5 7-5.5" fill="none" stroke="#1ea3dc" stroke-width="1.5"/></svg>
          email@homebridle-example.com
        </p>
        <p class="contact-row">
          <svg viewBox="0 0 16 16" aria-hidden="true"><g fill="none" stroke="#1ea3dc" stroke-width="1.2"><circle cx="8" cy="8" r="6.5"/><ellipse cx="8" cy="8" rx="2.8" ry="6.5"/><path d="M1.5 8h13M2.5 4.8h11M2.5 11.2h11"/></g></svg>
          www.homebridle.com
        </p>
      </div>
    </div>
    <svg class="foot-band" viewBox="0 0 593 16" aria-hidden="true">
      <polygon points="0,0 300,0 293,16 0,16" fill="#1a2430"/>
      <polygon points="300,0 303,0 296,16 293,16" fill="#f4f4f4"/>
      <polygon points="303,0 593,0 593,16 296,16" fill="#1ea3dc"/>
    </svg>
  </section>
</main>
</body>
</html>
```